Brightpath Coverage Partners
Stationary
Project: Brightpath Coverage Partners
Brightpath Coverage Partners -
Creative Brief
Professional
Dorian Fell
Agent / Broker
71362 West Maple Lane Ste. B Idyllwild, CA 92871-0517
dorian@brightpathcoverage.example
www.brightpathcoverage.example
Insurance License No: 0K72918
Please put the main lines of insurance I sell: Home, Auto, Commercial, Life, Health, Retirement

```html
<!DOCTYPE html>
<html lang="en">
<head>
<meta charset="utf-8">
<title>Brightpath Coverage Partners — Stationery</title>
<link rel="stylesheet" href="https://fonts.googleapis.com/css2?family=Lato:wght@300;400;700&display=swap">
<style>
:root{
  --navy:#123a78;
  --navy-deep:#0b2552;
  --blue:#2f64b3;
  --grey-dark:#3b3d42;
  --grey-mid:#8a8d93;
  --grey-line:#d5d8dd;
  --paper:#ffffff;
  --backdrop:#e9eaec;
  --ink:#2b2d31;
}
*{box-sizing:border-box;margin:0;padding:0}
html,body{width:1200px;height:917px;overflow:hidden}
body{background:var(--backdrop);font-family:"Lato",sans-serif;color:var(--ink);position:relative}
.sheet{position:absolute;background:var(--paper);box-shadow:0 2px 8px rgba(0,0,0,.18);overflow:hidden}
.brand{display:flex;align-items:center;gap:7px;color:var(--navy);font-weight:700;font-family:"Lato",sans-serif;line-height:1.1}
.brand-mark{width:16px;height:16px;background:var(--navy);flex:none}
.brand-name{font-size:12px;letter-spacing:.04em;text-transform:uppercase}

/* business card front */
.card-front{left:40px;top:40px;width:320px;height:183px;padding:22px}
.card-front .brand-name{font-size:11px;max-width:150px}
.card-person{position:absolute;right:22px;top:26px;text-align:right}
.card-person .name{font-size:15px;font-weight:700;color:var(--navy)}
.card-person .role{font-size:9px;color:var(--grey-mid);text-transform:uppercase;letter-spacing:.08em;margin-top:2px}
.card-contact{position:absolute;left:22px;right:22px;bottom:26px;font-size:8px;line-height:1.55;color:var(--grey-dark)}
.card-band{position:absolute;left:0;right:0;bottom:0;height:10px;background:linear-gradient(90deg,var(--navy-deep),var(--blue))}

/* business card back */
.card-back{left:40px;top:243px;width:320px;height:183px;background:linear-gradient(135deg,var(--navy-deep) 0 48%,var(--grey-dark) 48% 100%);display:flex;flex-direction:column;align-items:center;justify-content:center;gap:14px}
.card-back .brand{color:#fff}
.card-back .brand-mark{background:#fff}
.lines-of-insurance{font-size:8px;letter-spacing:.14em;color:#c9d3e6;text-transform:uppercase}

/* letterhead & fax */
.letterhead,.fax{top:40px;width:360px;height:466px;padding:28px 30px}
.letterhead{left:400px}
.fax{left:800px}
.sheet-head{display:flex;justify-content:space-between;align-items:flex-start;border-bottom:1px solid var(--grey-line);padding-bottom:12px}
.sheet-head .brand-name{font-size:11px;max-width:160px}
.fax-title{font-size:26px;font-weight:300;color:var(--navy);letter-spacing:.1em}
.letter-body{margin-top:40px;font-size:8px;line-height:1.7;color:var(--grey-dark)}
.letter-body p{margin-bottom:10px}
.signature{margin-top:18px;font-size:9px;font-weight:700;color:var(--navy)}
.sheet-foot{position:absolute;left:30px;right:30px;bottom:22px;font-size:7px;color:var(--grey-mid);text-align:center;line-height:1.6}
.sheet-band{position:absolute;left:0;right:0;bottom:0;height:6px;background:linear-gradient(90deg,var(--navy-deep),var(--blue))}

.fax-table{width:100%;margin-top:26px;border-collapse:collapse;font-size:8px}
.fax-table td{border-bottom:1px solid var(--grey-line);height:26px;color:var(--grey-dark)}
.fax-table td.label{width:52px;font-weight:700;color:var(--navy);text-transform:uppercase;letter-spacing:.06em}
.fax-checks{display:flex;gap:18px;margin-top:20px;font-size:8px;color:var(--grey-dark)}
.fax-checks span::before{content:"";display:inline-block;width:8px;height:8px;border:1px solid var(--grey-mid);margin-right:5px;vertical-align:-1px}
.fax-notes{margin-top:18px;height:120px;border:1px solid var(--grey-line)}

/* envelope */
.envelope{left:40px;top:540px;width:520px;height:226px;padding:22px}
.envelope .brand-name{font-size:11px;max-width:170px}
.envelope-return{font-size:8px;color:var(--grey-dark);margin-top:8px;line-height:1.5}
.envelope-sweep{position:absolute;left:0;bottom:0;width:100%;height:70px}

/* compliment slip */
.slip{left:600px;top:540px;width:560px;height:226px;padding:24px 28px}
.slip .brand-name{font-size:11px}
.slip-text{margin-top:30px;font-size:20px;font-weight:300;color:var(--navy);letter-spacing:.04em}
.slip-contact{position:absolute;left:28px;bottom:24px;font-size:8px;color:var(--grey-dark);line-height:1.6}
</style>
</head>
<body>

<section class="sheet card-front">
  <div class="brand"><span class="brand-mark"></span><span class="brand-name">Brightpath Coverage Partners</span></div>
  <div class="card-person">
    <div class="name">Dorian Fell</div>
    <div class="role">Agent / Broker</div>
  </div>
  <div class="card-contact">
    71362 West Maple Lane Ste. B Idyllwild, CA 92871-0517<br>
    dorian@brightpathcoverage.example<br>
    www.brightpathcoverage.example<br>
    Insurance License No: 0K72918
  </div>
  <div class="card-band"></div>
</section>

<section class="sheet card-back">
  <div class="brand"><span class="brand-mark"></span><span class="brand-name">Brightpath Coverage Partners</span></div>
  <div class="lines-of-insurance">Home · Auto · Commercial · Life · Health · Retirement</div>
</section>

<section class="sheet letterhead">
  <header class="sheet-head">
    <div class="brand"><span class="brand-mark"></span><span class="brand-name">Brightpath Coverage Partners</span></div>
  </header>
  <div class="letter-body">
    <p>Dear Client,</p>
    <p>Thank you for choosing us to protect what matters most. Our team reviews each policy with care so your coverage fits your life today and grows with you tomorrow.</p>
    <p>Please call us anytime with questions about home, auto, commercial, life, health or retirement plans.</p>
    <p>Sincerely,</p>
    <div class="signature">Dorian Fell<br><span style="font-weight:400;color:var(--grey-mid)">Agent / Broker</span></div>
  </div>
  <footer class="sheet-foot">71362 West Maple Lane Ste. B Idyllwild, CA 92871-0517 · www.brightpathcoverage.example<br>Insurance License No: 0K72918</footer>
  <div class="sheet-band"></div>
</section>

<section class="sheet fax">
  <header class="sheet-head">
    <div class="brand"><span class="brand-mark"></span><span class="brand-name">Brightpath Coverage Partners</span></div>
    <div class="fax-title">FAX</div>
  </header>
  <table class="fax-table">
    <tr><td class="label">To</td><td></td></tr>
    <tr><td class="label">From</td><td></td></tr>
    <tr><td class="label">Fax</td><td></td></tr>
    <tr><td class="label">Phone</td><td></td></tr>
    <tr><td class="label">Pages</td><td></td></tr>
    <tr><td class="label">Date</td><td></td></tr>
    <tr><td class="label">Re</td><td></td></tr>
  </table>
  <div class="fax-checks"><span>Urgent</span><span>For Review</span><span>Please Reply</span></div>
  <div class="fax-notes"></div>
  <footer class="sheet-foot">www.brightpathcoverage.example</footer>
  <div class="sheet-band"></div>
</section>

<section class="sheet envelope">
  <div class="brand"><span class="brand-mark"></span><span class="brand-name">Brightpath Coverage Partners</span></div>
  <div class="envelope-return">71362 West Maple Lane Ste. B<br>Idyllwild, CA 92871-0517</div>
  <svg class="envelope-sweep" viewBox="0 0 520 70" preserveAspectRatio="none" aria-hidden="true">
    <defs>
      <linearGradient id="sweep" x1="0" x2="1">
        <stop offset="0" stop-color="#0b2552"/>
        <stop offset="1" stop-color="#2f64b3"/>
      </linearGradient>
    </defs>
    <path d="M0 70 L0 40 C140 10 300 10 520 50 L520 70 Z" fill="url(#sweep)"/>
  </svg>
</section>

<section class="sheet slip">
  <div class="brand"><span class="brand-mark"></span><span class="brand-name">Brightpath Coverage Partners</span></div>
  <div class="slip-text">With Compliments</div>
  <div class="slip-contact">
    dorian@brightpathcoverage.example<br>
    www.brightpathcoverage.example
  </div>
  <div class="sheet-band"></div>
</section>

</body>
</html>
```